Harvest Velmora website and logo design

Looking to create a personal finance service website. My goal is for this website to be a resource repository where potential clients could come to get resources that they may find helpful for their personal use. I would like the website to have ways to collect emails from people who visit my website so I can send them periodic newsletters. I would like the website to have the following sections: A blog page, a resource page, a book review page (with potential affiliate links), An icon for a link to my podcast link ( titled Coin Climbers Working of getting this off the ground) ( I need a design for this podcast page as well) (coin climbers podcast is intended to interview everyday people who are on their journey to creating wealth, interview them and find out what is working for them) (design inspiration is an individual stacking a pile of gold) a section asking people to schedule a strategy coaching call, an about page.

I currently have a website with Word press titled Keliruston.com. The fron page should be about mira and a link to the harvest velmor platform. I would like to house harvest velmora on this site. I currently do not have a logo for harvest Velmora as well so I would like that or I can create a logo design request? The tag line should be Harvest Velmora… beside you. Helping your money grow branches.

The atmosphere I would like to have set for the site is that of calming colors that will put people at ease. The color green (vibrant green like that of a leaf) and gold is what I have in mind as my main color.
The vision of logo I have in mind to be incorporated through the website is that off a tree filled with money. The tree should have many roots and Coinage should be flowing through different channels of the roots. The goal is to teach people to give their money roots to go where they intend it to go rather than them wondering where their money went to every month.

The name of my business is harvest Velmora (pronounced: Velmoira). The idea is that harvest velmora with you. It does not escape you. So you are like a try planted and your money goes to where you intend them to go. You are intentional about your finance.

Target audience is men and women between the ages of 25-45. Core age is about 30 though. My targeted audience is the person who desires to have control over their finances by taking the appropriate action necessary. they are action oriented and go getters. They like to have resources at hand that will help them make informed decisions.
I would like images of real people looking at peace with the state of their well being.
Examples of websites I like are:
www.brightpursefolio.com/
https://www.tradelantern.com/
https://www.nadiquerovan.com/
https://velquist.tv/
https://maribelthorncrest.com/

Target Market(s)

Men and Women of all Race age 25-35

Logo Text

Harvest Velmora

Coding

Coded - Design and coding required

Number of Pages Required

4 page

Font styles to use
Serif
Decorative

Colors

Designer to choose colors to be used in the design.

```html
<!DOCTYPE html>
<html lang="en">
<head>
<meta charset="utf-8">
<title>Harvest Velmora</title>
<link href="https://fonts.googleapis.com/css2?family=Montserrat:wght@400;600;700;800&family=Open+Sans:wght@400;600&family=Oswald:wght@500;600&family=Playfair+Display:wght@700&display=swap" rel="stylesheet">
<style>
:root{
  --green:#0f8a3c;
  --green-dark:#0a5e2a;
  --green-light:#c9ecd3;
  --violet:#3a2a78;
  --ink:#2a2a2a;
  --muted:#6b6b6b;
  --line:#e4e4e4;
  --footer:#2c2c2c;
  --white:#ffffff;
}
*{box-sizing:border-box;margin:0;padding:0}
html,body{width:1200px;height:2968px;overflow:hidden;background:var(--white)}
body{font-family:"Open Sans",Arial,sans-serif;color:var(--ink);position:relative}
.abs{position:absolute}

/* header */
.site-header{position:absolute;top:0;left:0;width:1200px;height:120px;background:var(--white)}
.brand{position:absolute;left:235px;top:34px;display:flex;align-items:center;gap:10px}
.brand-dot{width:14px;height:14px;border-radius:50%;background:var(--green)}
.brand-name{font-family:"Montserrat",sans-serif;font-weight:700;font-size:19px;color:var(--green-dark);letter-spacing:1px}
.main-nav{position:absolute;right:240px;top:48px;display:flex;gap:20px;align-items:center;font-family:"Montserrat",sans-serif;font-size:11px;font-weight:600;color:var(--ink)}
.nav-search{width:22px;height:22px;border-radius:50%;background:var(--green)}

/* hero */
.hero{position:absolute;top:120px;left:0;width:1200px;height:412px;background:linear-gradient(110deg,#0c5a2c 0%,#14a04a 55%,#9fdcae 100%)}
.hero-photo{position:absolute;left:610px;top:0;width:300px;height:412px;background:linear-gradient(180deg,#6c4a3a,#a57a62 60%,#f1f1f1)}
.hero-title{position:absolute;left:230px;top:126px;font-family:"Montserrat",sans-serif;font-weight:800;font-size:40px;color:var(--white);letter-spacing:2px}
.hero-text{position:absolute;left:230px;top:180px;width:340px;font-size:13px;line-height:20px;color:var(--white)}
.btn{display:inline-block;font-family:"Montserrat",sans-serif;font-weight:700;font-size:10px;letter-spacing:1px;padding:11px 22px}
.btn-light{position:absolute;left:230px;top:240px;background:var(--white);color:var(--green-dark)}
.btn-green{background:var(--green);color:var(--white)}

/* about */
.about{position:absolute;top:532px;left:0;width:1200px;height:560px}
.about-square{position:absolute;background:var(--green-light)}
.eyebrow{font-family:"Montserrat",sans-serif;font-weight:700;font-size:15px;color:var(--green)}
.about-copy{position:absolute;left:232px;top:70px;width:340px}
.about-copy p{font-size:11px;line-height:19px;color:var(--muted);margin-top:14px}
.about-copy .btn{margin-top:28px}
.about-frame{position:absolute;left:630px;top:84px;width:250px;height:320px;background:var(--green)}
.about-photo{position:absolute;left:610px;top:64px;width:250px;height:320px;background:linear-gradient(160deg,#3c2b26,#8c6550 55%,#d7c2b5)}

/* business */
.business{position:absolute;top:1092px;left:0;width:1200px;height:440px;background:linear-gradient(100deg,#0f7a39 0%,#1b5d4a 40%,#2e3a78 75%,#3a2a78 100%)}
.business-photo{position:absolute;left:170px;top:40px;width:330px;height:400px;background:linear-gradient(180deg,#5e4134,#9c735e 60%,#e9e9e9)}
.business-copy{position:absolute;left:580px;top:80px;width:360px;color:var(--white)}
.business-copy .kicker{font-family:"Montserrat",sans-serif;font-weight:600;font-size:14px}
.business-copy h2{font-family:"Oswald",sans-serif;font-weight:600;font-size:38px;letter-spacing:1px;margin-top:2px}
.business-copy p{font-size:11px;line-height:19px;margin-top:14px;opacity:.9}

/* press */
.press{position:absolute;top:1532px;left:0;width:1200px;height:330px}
.section-title{font-family:"Montserrat",sans-serif;font-weight:700;font-size:15px;letter-spacing:1px;color:var(--green);text-align:center}
.press .section-title{position:absolute;top:40px;width:100%}
.press-grid{position:absolute;left:300px;top:110px;width:600px;display:grid;grid-template-columns:repeat(4,1fr);row-gap:38px;align-items:center;text-align:center}
.press-name{font-family:"Montserrat",sans-serif;font-weight:700;font-size:24px;color:#8a8a8a}

/* video */
.video{position:absolute;left:470px;top:1872px;width:370px;height:260px;background:linear-gradient(180deg,#b9b4ad,#7a5a48 55%,#d9d9d9)}
.play{position:absolute;left:165px;top:110px;width:42px;height:42px}

/* news */
.news{position:absolute;top:2160px;left:0;width:1200px;height:460px}
.news .section-title{position:absolute;top:28px;width:100%}
.news-grid{position:absolute;left:232px;top:88px;display:flex;gap:18px}
.card{width:235px}
.card-img{position:relative;height:150px;background:linear-gradient(150deg,#dfe7ea,#a8b9bf)}
.date-badge{position:absolute;left:14px;top:0;width:40px;height:42px;background:var(--green);color:var(--white);font-family:"Montserrat",sans-serif;font-size:10px;font-weight:700;text-align:center;line-height:14px;padding-top:7px}
.card h3{font-family:"Montserrat",sans-serif;font-weight:700;font-size:14px;line-height:19px;margin-top:16px}
.card p{font-size:10px;line-height:16px;color:var(--muted);margin-top:10px}
.read-more{display:block;font-family:"Montserrat",sans-serif;font-weight:700;font-size:9px;color:var(--green);margin-top:12px;letter-spacing:.5px}

/* footer */
.site-footer{position:absolute;top:2620px;left:0;width:1200px;height:348px;background:var(--footer);color:#cfcfcf}
.footer-brand{position:absolute;top:56px;width:100%;display:flex;justify-content:center;align-items:center;gap:10px}
.footer-brand .brand-name{color:var(--white)}
.social{position:absolute;top:150px;width:100%;display:flex;justify-content:center;gap:22px}
.social span{width:18px;height:18px;border-radius:50%;background:#cfcfcf}
.footer-nav{position:absolute;top:200px;width:100%;display:flex;justify-content:center;gap:24px;font-family:"Montserrat",sans-serif;font-size:10px;font-weight:700;color:var(--white)}
.copyright{position:absolute;top:248px;width:100%;text-align:center;font-size:10px}
</style>
</head>
<body>

<header class="site-header">
  <div class="brand"><span class="brand-dot"></span><span class="brand-name">HARVEST VELMORA</span></div>
  <nav class="main-nav">
    <span>About</span><span>Courses</span><span>Academy</span><span>Podcast</span><span>Articles</span><span>Store</span><span>News</span><span>Login</span><span class="nav-search"></span>
  </nav>
</header>

<section class="hero">
  <div class="hero-photo" role="img" aria-label="Portrait of a smiling woman in a white top"></div>
  <h1 class="hero-title">HI I'M VELMORA</h1>
  <p class="hero-text">Lorem ipsum dolor sit amet, consectetur adipiscing elit. Nunc nec massa dignissim, auctor erat a, tempus nisl.</p>
  <span class="btn btn-light">MORE ABOUT ME</span>
</section>

<section class="about">
  <div class="about-square" style="left:1000px;top:40px;width:90px;height:90px"></div>
  <div class="about-square" style="left:1090px;top:0;width:110px;height:110px;opacity:.6"></div>
  <div class="about-square" style="left:940px;top:150px;width:70px;height:70px;opacity:.7"></div>
  <div class="about-square" style="left:1040px;top:200px;width:120px;height:120px;opacity:.5"></div>
  <div class="about-copy">
    <div class="eyebrow">Learn More About</div>
    <p>Lorem ipsum dolor sit amet, consectetur adipiscing elit. Nunc nec massa dignissim, auctor erat a, tempus nisl. Vestibulum quis leo sed diam volutpat tincidunt. Curabitur convallis nulla non porttitor dapibus. Vestibulum et lacus efficitur, finibus lorem vel, pellentesque neque. Proin sed nisi vel justo cursus rutrum.</p>
    <p>Sed lacinia mi ac ultricies ultricies. Cras tempor odio nec consectetur. Ut ac condimentum nibh ipsum eget sapien. Vivamus id dolor quis lorem aliquet dapibus. Nulla ac tellus sed ligula hendrerit ullamcorper. Integer mattis velit nec eget sem.</p>
    <span class="btn btn-green">MY STORY</span>
  </div>
  <div class="about-frame"></div>
  <div class="about-photo" role="img" aria-label="Portrait of a woman wearing a pearl necklace"></div>
</section>

<section class="business">
  <div class="business-photo" role="img" aria-label="Smiling woman resting her chin on her hand"></div>
  <div class="business-copy">
    <div class="kicker">The Story Behind</div>
    <h2>OUR BUSINESS</h2>
    <p>Lorem ipsum dolor sit amet, consectetur adipiscing elit. Nunc nec massa dignissim, auctor erat a, tempus nisl. Vestibulum quis leo sed diam volutpat tincidunt. Curabitur convallis nulla non porttitor dapibus. Proin sed nisi vel justo cursus rutrum, et luctus.</p>
    <p>Sed lacinia mi ac ultricies ultricies. Cras tempor odio nec consectetur. Ut ac condimentum nibh ipsum eget sapien aliquet.</p>
  </div>
</section>

<section class="press">
  <h2 class="section-title">FEATURED IN THE PRESS</h2>
  <div class="press-grid">
    <span class="press-name">Coinage</span><span class="press-name">Swiftworks</span><span class="press-name">Morning Bright</span><span class="press-name">Lustre</span>
    <span class="press-name">Kernel</span><span class="press-name">Newsline</span><span class="press-name">Tradewire</span><span class="press-name">Fortis</span>
  </div>
</section>

<div class="video" role="img" aria-label="Video still of a smiling woman">
  <svg class="play" viewBox="0 0 42 42"><circle cx="21" cy="21" r="21" fill="#0f8a3c"/><path d="M17 13 L30 21 L17 29 Z" fill="#fff"/></svg>
</div>

<section class="news">
  <h2 class="section-title">NEWS &amp; ARTICLES</h2>
  <div class="news-grid">
    <article class="card">
      <div class="card-img" role="img" aria-label="Doctor speaking with a patient"><div class="date-badge">15<br>DEC</div></div>
      <h3>Lorem ipsum dolor sit amet consectetur adipiscing elit.</h3>
      <p>Ut consectetur facilisis ultricies. Suspendisse sed maximus orci. Praesent quis magna.</p>
      <span class="read-more">READ MORE</span>
    </article>
    <article class="card">
      <div class="card-img" role="img" aria-label="Nurse caring for a patient"><div class="date-badge">15<br>DEC</div></div>
      <h3>Lorem ipsum dolor sit amet consectetur adipiscing elit.</h3>
      <p>Ut consectetur facilisis ultricies. Suspendisse sed maximus orci. Praesent quis magna.</p>
      <span class="read-more">READ MORE</span>
    </article>
    <article class="card">
      <div class="card-img" role="img" aria-label="Medical team in a bright room"><div class="date-badge">15<br>DEC</div></div>
      <h3>Lorem ipsum dolor sit amet consectetur adipiscing elit.</h3>
      <p>Ut consectetur facilisis ultricies. Suspendisse sed maximus orci. Praesent quis magna.</p>
      <span class="read-more">READ MORE</span>
    </article>
  </div>
</section>

<footer class="site-footer">
  <div class="footer-brand"><span class="brand-dot"></span><span class="brand-name">HARVEST VELMORA</span></div>
  <div class="social"><span></span><span></span><span></span><span></span><span></span></div>
  <nav class="footer-nav"><span>ABOUT</span><span>COURSES</span><span>ACADEMY</span><span>PODCAST</span><span>ARTICLES</span><span>EVENT</span><span>STORE</span><span>LOGIN</span></nav>
  <div class="copyright">Copyright © 2020 Harvest Velmora. All rights reserved.</div>
</footer>

</body>
</html>
```